Classic and neutral book cover design

We are looking for a classic and neutral book cover design to be used as the template for a series of books to be published. We are hence looking for a template that will allow us to easily change the title name for all books in this series.
The use of very few colours (black and white is welcome) and few design elements is a big bonus. As a source of inspiration we would like to ask you to view the very simple and
If you think you have a cool idea that can add a twist to the formal classic look don't hesitate. Go for it !
Work will be done for a 30 year old Sweden based cultural non-profit called VĂ©lra (www.velrafoundation.example). We work with the publishing and supporting of post-modern art and literature addressing contemporary topics but are also involved in assisting projects of cultural preservation.
Target Market(s)
The audience is expected to have some form of interest in culture but could range from hobbyist readers to tenure track scholars
Industry/Entity Type
Non-Profit
Requirements
Must have
- General:
- Classic and neutral feel
- Preferably very simple and few shapes
- usage of few colours (black and white is welcome)
Information to be displayed on the cover is:
- Author
- Title
- type of work e.g. play/novel (optional)
- publishing house (in this case "Velra Publishing")
Nice to have
- ideas to prevent it from become boring are of course welcome
Should not have
- - too many colours

```html
<!DOCTYPE html>
<html lang="en">
<head>
<meta charset="utf-8">
<title>Velra Publishing – Book Cover</title>
<link rel="stylesheet" href="https://fonts.googleapis.com/css2?family=Crimson+Text:ital,wght@0,400;1,400&display=swap">
<style>
  :root {
    --paper: #ffffff;
    --ink: #111111;
    --photo-light: #e6e6e6;
    --photo-mid: #8a8a8a;
    --photo-dark: #1a1a1a;
  }
  html, body {
    margin: 0;
    padding: 0;
    overflow: hidden;
    background: var(--paper);
  }
  .cover {
    position: relative;
    width: 952px;
    height: 1200px;
    background: var(--paper);
    font-family: "Crimson Text", Georgia, serif;
    color: var(--ink);
    overflow: hidden;
  }
  .frame {
    position: absolute;
    border: 2px solid var(--ink);
    box-sizing: border-box;
  }
  .frame--outer { left: 42px; top: 42px; width: 868px; height: 1120px; }
  .frame--inner { left: 57px; top: 57px; width: 838px; height: 1090px; }
  .shards {
    position: absolute;
    inset: 0;
  }
  .line {
    position: absolute;
    left: 0;
    width: 100%;
    margin: 0;
    text-align: center;
    line-height: 1;
    font-weight: 400;
  }
  .publisher {
    top: 179px;
    font-size: 18px;
    font-style: italic;
    letter-spacing: 0.16em;
    text-transform: uppercase;
  }
  .title {
    top: 334px;
    font-size: 88px;
    letter-spacing: 0.2em;
    padding-left: 0.2em;
    box-sizing: border-box;
  }
  .work-type {
    top: 781px;
    font-size: 27px;
    font-style: italic;
  }
  .by {
    top: 838px;
    font-size: 17px;
    font-style: italic;
  }
  .author {
    top: 868px;
    font-size: 30px;
    letter-spacing: 0.12em;
  }
</style>
</head>
<body>
  <main class="cover">
    <div class="frame frame--outer"></div>
    <div class="frame frame--inner"></div>

    <svg class="shards" width="952" height="1200" viewBox="0 0 952 1200" aria-hidden="false">
      <defs>
        <linearGradient id="shard-tone-a" x1="0" y1="0" x2="1" y2="0.3">
          <stop offset="0" stop-color="var(--photo-dark)"/>
          <stop offset="0.55" stop-color="var(--photo-mid)"/>
          <stop offset="1" stop-color="var(--photo-light)"/>
        </linearGradient>
        <linearGradient id="shard-tone-b" x1="0" y1="0" x2="1" y2="0.6">
          <stop offset="0" stop-color="var(--photo-light)"/>
          <stop offset="0.5" stop-color="var(--photo-mid)"/>
          <stop offset="1" stop-color="var(--photo-dark)"/>
        </linearGradient>
        <linearGradient id="shard-tone-c" x1="0" y1="0" x2="0.4" y2="1">
          <stop offset="0" stop-color="var(--photo-mid)"/>
          <stop offset="1" stop-color="var(--photo-dark)"/>
        </linearGradient>
      </defs>
      <polygon class="shard shard--small" role="img" aria-label="Fragment of a blurred black and white photograph"
               points="659,218 812,245 695,299" fill="url(#shard-tone-a)"/>
      <polygon class="shard shard--large" role="img" aria-label="Fragment of a blurred black and white photograph of dark vertical forms"
               points="500,473 677,745 247,637" fill="url(#shard-tone-b)"/>
      <polygon class="shard shard--corner" role="img" aria-label="Fragment of a blurred black and white photograph"
               points="221,901 96,987 175,1102" fill="url(#shard-tone-c)"/>
    </svg>

    <p class="line publisher">Velra Publishing</p>
    <h1 class="line title">NICE TITLE</h1>
    <p class="line work-type">Novel</p>
    <p class="line by">by</p>
    <p class="line author">Author Authorson</p>
  </main>
</body>
</html>
```